Brochure for Specialist Divorce Support

1. I want an A4 three fold brochure or DL to promote my business and services.
My market are people going through divorce and are usually feeling very overwhelmed and therefore not functioning very well - both men and women, age early forties,
2. Colours – variety of blues and lime greens but you choose if you need a contrast e.g. orange
3. Images – happy single families
4. Theme - could you make it around water please - soothing
5. Logos – KFT &; KFN (I will attach)
6. I have a lot of content so maybe not too busy but still professional feel +
warm and reassuring
7. I'm attaching -

- a draft brochure I put together using a Microsoft template
- a word document with extra details
- plus two logos to do with my qualifications
- and some images for you to choose from

7. I want to use this as a template for some other brochures -> more work for
the winner.

Target Market(s)

Men and women usually in their early forties with primary school aged children i.e 5 to 12 years old.
They are going through a divorce and very upset, Maybe losing contact with their children and their way of life as they know it is disappearing. They are in turmoil and not functioning as well as they usually do.

Industry/Entity Type

Business

Font styles to use
Sans Serif

Colors
34a7d7
abd037
3277b5

Requirements
Must have
• I want the brochure to be three folds with the center the full A4
• Could you make the theme around water please.
• I will upload some photos for you to use if you want,

```html
<!DOCTYPE html>
<html lang="en">
<head>
<meta charset="utf-8">
<title>Divorce Coaching Brochure</title>
<link href="https://fonts.googleapis.com/css2?family=Open+Sans:wght@400;600;700&display=swap" rel="stylesheet">
<style>
:root{
  --bg:#e4e6e9;
  --paper:#ffffff;
  --navy:#1d4f9c;
  --blue:#2463b3;
  --sky:#34a7d7;
  --lime:#7dbf2a;
  --lime-light:#a6d23a;
  --orange:#f6a81c;
  --ink:#4a4f55;
  --rule:#c9ced4;
  --photo-warm:#e9d3c4;
  --photo-cool:#dfe6ee;
}
*{box-sizing:border-box;margin:0;padding:0}
html,body{width:857px;height:1200px;overflow:hidden}
body{background:var(--bg);font-family:"Open Sans",Arial,sans-serif;color:var(--ink);position:relative}
.sheet{position:absolute;left:60px;width:737px;background:var(--paper);overflow:hidden;box-shadow:0 2px 6px rgba(0,0,0,.25)}
.sheet--outside{top:57px;height:520px}
.sheet--inside{top:624px;height:519px}
.panel{position:absolute;top:0;height:100%;width:245.6px}
.panel--1{left:0}
.panel--2{left:245.6px}
.panel--3{left:491.2px}
.fold{position:absolute;top:0;bottom:0;width:1px;background:rgba(0,0,0,.06);z-index:5}
.waves{position:absolute;left:0;top:0;width:100%;height:100%;z-index:2}
.photo{position:absolute;z-index:1}
.above{position:relative;z-index:3}
.h-section{font-size:12px;color:var(--ink);font-weight:400;letter-spacing:.2px;padding-bottom:5px;border-bottom:1px solid var(--rule);margin-bottom:10px;white-space:nowrap}
.h-section b{color:var(--navy);font-weight:700}
.list{list-style:none}
.list li{position:relative;padding-left:16px;font-size:8px;line-height:1.45;margin-bottom:10px}
.list li svg{position:absolute;left:0;top:1px;width:10px;height:10px}
.list--compact li{font-size:7.4px;line-height:11px;margin-bottom:6.5px}
.site{position:absolute;bottom:11px;left:0;right:0;text-align:center;font-size:10.5px;color:var(--navy);z-index:4;display:flex;justify-content:center;align-items:center;gap:6px}
.site svg{width:10px;height:10px}
.wordmark{display:flex;align-items:center;justify-content:center;gap:6px;font-weight:700;color:var(--navy);font-size:30px;letter-spacing:1px}
.wordmark i{display:block;width:14px;height:14px;background:var(--navy)}
.contact-note{font-size:10px;color:var(--blue);text-align:center;line-height:1.5;margin-top:14px}
.details{margin:10px 28px 0;border:1px solid var(--lime);padding:12px 6px 10px;text-align:center;font-size:10px;line-height:1.55;color:#333}
.details .label{color:var(--blue);font-size:10.5px;background:#fff;margin:-19px auto 4px;width:max-content;padding:0 4px}
.details .alt{color:var(--blue)}
.phone-btn{display:flex;align-items:center;justify-content:center;gap:5px;margin:-8px auto 0;width:118px;height:20px;border-radius:3px;background:var(--lime);color:#fff;font-weight:700;font-size:11px;position:relative}
.phone-btn svg{width:10px;height:10px}
.quote{position:absolute;left:20px;right:20px;top:418px;text-align:center;font-size:14.5px;line-height:1.55;color:#1f3a2c;z-index:4}
.stage{font-size:7.2px;line-height:1.45;margin-bottom:8px}
.stage h3{font-size:8px;color:var(--blue);font-weight:400;margin-bottom:1px}
.center-title{font-size:9px;color:var(--navy);font-weight:700;text-align:center;margin-top:12px;white-space:nowrap}
.center-lead{text-align:center;font-size:11px;line-height:1.5;margin-top:10px;color:#333}
.center-accent{text-align:center;font-size:11px;color:var(--blue);font-weight:600;margin-top:8px}
.center-small{text-align:center;font-size:8.5px;line-height:1.5;margin-top:10px;color:#333}
.skills-title{font-size:10px;color:var(--navy);font-weight:700}
.skills-sub{font-size:10px;color:#444;margin-bottom:6px}
.ticks{list-style:none}
.ticks li{position:relative;padding-left:10px;font-size:6.8px;line-height:1.35;margin-bottom:2.5px}
.ticks li::before{content:"✓";position:absolute;left:0;color:var(--blue);font-size:7px}
.moving-title{font-size:10.5px;color:var(--navy);font-weight:700;margin-top:7px}
.moving-sub{font-size:10px;color:#444}
.moving-intro{font-size:7.5px;color:#333;margin:4px 0 3px}
.pace{font-size:9.5px;font-weight:700;color:var(--navy);line-height:1.4;margin-top:7px;width:190px}
.pace span{display:block;width:70px}
.circle{position:absolute;border-radius:50%;border:7px solid var(--orange);z-index:3}
</style>
</head>
<body>

<section class="sheet sheet--outside">
  <div class="photo" role="img" aria-label="Photo of a smiling mother hugging her young daughter" style="left:40px;top:275px;width:200px;height:215px;background:radial-gradient(ellipse at 50% 45%,var(--photo-warm),#f4ece6 70%,#fff)"></div>
  <div class="photo" role="img" aria-label="Photo of a smiling father carrying his daughter, who kisses his cheek" style="left:260px;top:260px;width:220px;height:235px;background:radial-gradient(ellipse at 50% 50%,#c98a7a,#e9d6cc 60%,#f4f1ee)"></div>
  <div class="photo" role="img" aria-label="Photo of a laughing mother and daughter in hair curlers sharing a kiss" style="left:491px;top:0;width:246px;height:420px;background:linear-gradient(180deg,#e8eef5 0%,var(--photo-warm) 45%,#d98a9f 80%,#c9b8c8 100%)"></div>

  <svg class="waves" viewBox="0 0 737 520" preserveAspectRatio="none" aria-hidden="true">
    <defs>
      <linearGradient id="g-lime" x1="0" y1="0" x2="1" y2="0">
        <stop offset="0" stop-color="#7cc22a"/><stop offset="1" stop-color="#5fb22a"/>
      </linearGradient>
      <linearGradient id="g-blue" x1="0" y1="0" x2="1" y2="0">
        <stop offset="0" stop-color="#1f4f9e"/><stop offset=".6" stop-color="#2a76c8"/><stop offset="1" stop-color="#1f5fae"/>
      </linearGradient>
    </defs>
    <path d="M0,372 C90,410 170,450 270,470 L262,480 C160,466 80,440 0,402Z" fill="var(--orange)"/>
    <path d="M0,402 C80,440 160,466 262,480 L250,490 C160,482 80,460 0,430Z" fill="#e7e9ec"/>
    <path d="M0,430 C150,470 250,500 360,495 C500,488 600,400 737,380 L737,520 L0,520Z" fill="url(#g-lime)"/>
    <path d="M140,498 C300,505 480,420 737,356 L737,378 C600,400 500,486 360,494 C280,498 200,500 140,498Z" fill="url(#g-blue)"/>
  </svg>

  <div class="fold" style="left:245.6px"></div>
  <div class="fold" style="left:491.2px"></div>

  <div class="panel panel--1">
    <div class="above" style="padding:22px 28px 0 26px">
      <h2 class="h-section"><b>MY</b> SERVICES:</h2>
      <ul class="list">
        <li><svg viewBox="0 0 10 10"><path d="M1,1 L9,5 L1,9 L3,5Z" fill="var(--blue)"/></svg>Tailored divorce support to suit your needs</li>
        <li><svg viewBox="0 0 10 10"><path d="M1,1 L9,5 L1,9 L3,5Z" fill="var(--blue)"/></svg>Pre-mediation coaching helping you prepare and achieve more positive outcomes to avoid court</li>
        <li><svg viewBox="0 0 10 10"><path d="M1,1 L9,5 L1,9 L3,5Z" fill="var(--blue)"/></svg>Collaborative law coaching to increase crucial skills so you can participate more constructively in negotiations</li>
        <li><svg viewBox="0 0 10 10"><path d="M1,1 L9,5 L1,9 L3,5Z" fill="var(--blue)"/></svg>Delivery of KFT Key Friction Tracker giving you real feedback on the constructive and destructive behaviours you choose during conflict situations to facilitate more productive discussions</li>
        <li><svg viewBox="0 0 10 10"><path d="M1,1 L9,5 L1,9 L3,5Z" fill="var(--blue)"/></svg>Corporate Conflict Management Training</li>
      </ul>
    </div>
    <div class="site"><svg viewBox="0 0 10 10"><circle cx="5" cy="5" r="4.2" fill="none" stroke="var(--navy)"/><path d="M1,5H9M5,1C3,3 3,7 5,9M5,1C7,3 7,7 5,9" fill="none" stroke="var(--navy)" stroke-width=".7"/></svg>SteadyShoreCoaching.com.au</div>
  </div>

  <div class="panel panel--2">
    <div class="above" style="padding-top:26px">
      <div class="wordmark"><i></i>KFN</div>
      <p class="contact-note">Coaching works well over the phone,<br>allowing for flexibility of time and place -<br>evening appointments available.</p>
      <div class="details">
        <div class="label">FULL DETAILS ARE ON:</div>
        SteadyShoreCoaching.com.au<br>
        <span class="alt">or email:</span><br>
        Helen@CalmWaterSupport.com.au
      </div>
      <div class="phone-btn"><svg viewBox="0 0 10 10"><circle cx="5" cy="5" r="4.4" fill="none" stroke="#fff"/><path d="M3.4,2.8 4.3,2.6 4.8,3.9 4.2,4.4C4.5,5 5,5.5 5.6,5.8L6.1,5.2 7.4,5.7 7.2,6.6C5.2,6.8 3.2,4.8 3.4,2.8Z" fill="#fff"/></svg>0400 123 456</div>
    </div>
    <div class="site"><svg viewBox="0 0 10 10"><circle cx="5" cy="5" r="4.2" fill="none" stroke="var(--navy)"/><path d="M1,5H9M5,1C3,3 3,7 5,9M5,1C7,3 7,7 5,9" fill="none" stroke="var(--navy)" stroke-width=".7"/></svg>SteadyShoreCoaching.com.au</div>
  </div>

  <div class="panel panel--3">
    <div class="above" style="padding-top:28px">
      <div class="wordmark" style="font-size:26px"><i></i>KFT</div>
    </div>
    <p class="quote">Everyone is different<br>and move through these<br>stages at their own pace</p>
    <div class="site"><svg viewBox="0 0 10 10"><circle cx="5" cy="5" r="4.2" fill="none" stroke="var(--navy)"/><path d="M1,5H9M5,1C3,3 3,7 5,9M5,1C7,3 7,7 5,9" fill="none" stroke="var(--navy)" stroke-width=".7"/></svg>SteadyShoreCoaching.com.au</div>
  </div>
</section>

<section class="sheet sheet--inside">
  <svg class="waves" viewBox="0 0 737 519" preserveAspectRatio="none" aria-hidden="true">
    <defs>
      <linearGradient id="g-lime2" x1="0" y1="0" x2="1" y2="0">
        <stop offset="0" stop-color="#7cc22a"/><stop offset="1" stop-color="#5fb22a"/>
      </linearGradient>
      <linearGradient id="g-blue2" x1="0" y1="0" x2="1" y2="0">
        <stop offset="0" stop-color="#1f4f9e"/><stop offset=".6" stop-color="#2a76c8"/><stop offset="1" stop-color="#1f5fae"/>
      </linearGradient>
    </defs>
    <path d="M0,318 C150,340 250,440 380,465 C420,480 440,500 460,519 L0,519Z" fill="url(#g-lime2)"/>
    <path d="M560,519 C640,490 690,450 737,420 L737,519Z" fill="url(#g-lime2)"/>
    <path d="M0,300 C150,320 250,420 380,450 C520,475 640,455 737,400 L737,420 C640,475 520,492 380,466 C250,440 150,338 0,318Z" fill="url(#g-blue2)"/>
  </svg>

  <div class="fold" style="left:245.6px"></div>
  <div class="fold" style="left:491.2px"></div>

  <div class="panel panel--1">
    <div class="above" style="padding:20px 24px 0 22px">
      <h2 class="h-section"><b>COACHING</b> CAN HELP YOU:</h2>
      <ul class="list list--compact">
        <li><svg viewBox="0 0 10 10"><path d="M1,1 L9,5 L1,9 L3,5Z" fill="var(--lime)"/></svg>Save money by being a more collected and credible client in the legal process</li>
        <li><svg viewBox="0 0 10 10"><path d="M1,1 L9,5 L1,9 L3,5Z" fill="var(--lime)"/></svg>Stay in control and focus on what's important for you and your family to avoid angry, emotional hijacks</li>
        <li><svg viewBox="0 0 10 10"><path d="M1,1 L9,5 L1,9 L3,5Z" fill="var(--lime)"/></svg>Feel more empowered by being organised and prepared for what's ahead and develop a plan of action</li>
        <li><svg viewBox="0 0 10 10"><path d="M1,1 L9,5 L1,9 L3,5Z" fill="var(--lime)"/></svg>Identify your next steps re: legal, financial, children's issues plus your self-care</li>
        <li><svg viewBox="0 0 10 10"><path d="M1,1 L9,5 L1,9 L3,5Z" fill="var(--lime)"/></svg>Develop a draft parenting plan to anticipate and address possible issues</li>
        <li><svg viewBox="0 0 10 10"><path d="M1,1 L9,5 L1,9 L3,5Z" fill="var(--lime)"/></svg>Consider areas of possible conflict and explore techniques to reduce confrontation</li>
        <li><svg viewBox="0 0 10 10"><path d="M1,1 L9,5 L1,9 L3,5Z" fill="var(--lime)"/></svg>Find your voice and be more confident in your skills to take control of your divorce and do it your way</li>
        <li><svg viewBox="0 0 10 10"><path d="M1,1 L9,5 L1,9 L3,5Z" fill="var(--lime)"/></svg>Let go of what was ... and create what is possible during your divorce journey and afterwards.</li>
      </ul>
    </div>
    <div class="circle" role="img" aria-label="Photo of a mother and young daughter cuddling cheek to cheek" style="left:30px;top:316px;width:182px;height:182px;background:radial-gradient(circle at 50% 45%,#f3e2d2,var(--photo-warm) 60%,#d8c3b3)"></div>
  </div>

  <div class="panel panel--2">
    <div class="above" style="padding:20px 18px 0 20px">
      <h2 class="h-section" style="font-size:9.6px"><b>YOU WILL GO THROUGH</b> DISTINCT STAGES:</h2>
      <div class="stage">
        <h3>1.The Preparation Stage – maybe entail one or two coaching sessions</h3>
        Anticipating all the unknowns and preparing before you see a Family Law Solicitor can save a lot of your solicitor's time and therefore money. The clearer you are on what you want to achieve throughout the process, the more specific legal advice you will receive.
      </div>
      <div class="stage">
        <h3>2.The Business Side of Divorce – maybe two to four coaching sessions</h3>
        Divorce involves multiple areas of change, intensity of emotions, life changing decisions, loss of family structure and often a sense of isolation not experienced before.<br>
        The emotional overwhelm associated with relationship breakdown and the associated loss of 24/7 contact with children can impact even the most together person's ability to make well considered decisions.<br>
        Together, we will process emotions constructively and clarify decisions to be made... for you to be better able to communicate these in negotiations as well as set new boundaries.
      </div>
      <p class="center-title">TAILORED DIVORCE COACHING /SUPPORT</p>
      <p class="center-lead">Helping you successfully navigate<br>this major life challenge ...</p>
      <p class="center-accent">and move forward to your new life!</p>
      <p class="center-small">Together we will identify your goals,<br>set priorities and develop a plan for tomorrow ...<br>moving you through the pain of divorce.</p>
    </div>
    <div class="site"><svg viewBox="0 0 10 10"><circle cx="5" cy="5" r="4.2" fill="none" stroke="var(--navy)"/><path d="M1,5H9M5,1C3,3 3,7 5,9M5,1C7,3 7,7 5,9" fill="none" stroke="var(--navy)" stroke-width=".7"/></svg>SteadyShoreCoaching.com.au</div>
  </div>

  <div class="panel panel--3">
    <div class="above" style="padding:20px 16px 0 22px">
      <p class="skills-title">Where Necessary We Can Work On Skills</p>
      <p class="skills-sub">You Will Need For Successful Outcomes:</p>
      <ul class="ticks">
        <li>Conflict resolution skills plus specific verbal &amp; written communication skills important for more neutral emails and messages</li>
        <li>Having difficult conversations</li>
        <li>Preparing before attending joint conferences or mediation</li>
        <li>Managing anger</li>
        <li>Supporting your children to also navigate changed family structures</li>
        <li>Grieving losses ... even if you are the one who made the decision to leave<br>Strategies for you to start healing and become whole again</li>
        <li>Drafting a parenting plan to anticipate &amp; address possible parenting issues, leading to more positive and successful co-parenting in the long term.</li>
        <li>This is in everyone's interests... especially your children's.</li>
        <li>Look at possible stress strategies to sustain your energy levels, important for you to make good considered decisions</li>
      </ul>
      <p class="moving-title">The Moving On Stage –</p>
      <p class="moving-sub">One Or Two Coaching Sessions</p>
      <p class="moving-intro">Dealing with endings and focusing on the future:</p>
      <ul class="ticks">
        <li>Changing your "self" image and building self worth</li>
        <li>Transitioning from married life to being single again</li>
        <li>Address barriers preventing you from moving forward</li>
        <li>Setting realistic goals to help transition to your new life more effectively</li>
      </ul>
      <p class="pace">EVERYONE IS DIFFERENT AND MOVES <span>THROUGH THE STAGES AT THEIR OWN PACE.</span></p>
    </div>
    <div class="circle" role="img" aria-label="Photo of a smiling father holding his young daughter" style="left:104px;top:380px;width:118px;height:118px;background:radial-gradient(circle at 50% 45%,#e6cdbb,#c99b84 60%,#e3e6ea)"></div>
  </div>
</section>

</body>
</html>
```